Magazine Cover & Back, Course Overview

Please read this whole description and follow directions before proceeding. Please do not submit multiple designs that look similar. If you submit multiple designs that look similar you will be disqualified and receive a poor rating. A magazine design includes a cover and back. This is a single design and should be submitted as such. Do not submit one design for the front only, then a separate design for the back, then a third mock up. Submit all as a single design. I need a magazine cover and back. The size will be standard paper size, 8-1/2" x 11". It will be used for a course overview, a summary of a boating instruction course. I have attached examples and pictures that can be used. I have also attached required content. The final designs must NOT be AI files. Text must be editable with Adobe Acrobat DC.

Target Market(s)

Military & Government

Industry/Entity Type

Military & Government

Requirements
Must have
• See attached.
Nice to have
• See attached.
Should not have
• See attached.

```html
<!DOCTYPE html>
<html lang="en">
<head>
<meta charset="utf-8">
<title>Harbor Compass Marine Services – Course Overview</title>
<link rel="stylesheet" href="https://fonts.googleapis.com/css2?family=Montserrat:wght@700&family=Playfair+Display:ital,wght@0,700;0,900;1,700&display=swap">
<style>
  :root {
    --backdrop: #2a3039;
    --paper: #ffffff;
    --navy: #1b2a6b;
    --royal: #3344b8;
    --royal-light: #5567d6;
    --red: #a50f12;
    --steel: #5f6368;
    --sky: #8fb6e6;
    --hull: #a9adb2;
    --white: #ffffff;
  }
  * { margin: 0; padding: 0; box-sizing: border-box; }
  html, body { width: 835px; height: 1200px; overflow: hidden; }
  body {
    background: var(--backdrop);
    position: relative;
    font-family: "Playfair Display", serif;
  }
  .page {
    position: absolute;
    top: 347px;
    width: 390px;
    height: 505px;
    background: var(--paper);
    overflow: hidden;
  }
  .page--front { left: 17px; }
  .page--back { left: 428px; }

  /* Brand lockup */
  .brand { position: absolute; top: 40px; left: 55px; display: flex; align-items: center; gap: 10px; }
  .brand__mark { width: 60px; height: 60px; border-radius: 50%; background: var(--steel); flex: none; }
  .brand__name {
    font-family: "Playfair Display", serif; font-weight: 700; color: var(--steel);
    font-size: 25px; line-height: 1.05;
  }
  .brand__name small { display: block; font-size: 13px; letter-spacing: 1.5px; margin-top: 4px; }

  /* Front */
  .course-label {
    position: absolute; top: 120px; left: 0; width: 390px; text-align: center;
    font-family: "Montserrat", sans-serif; font-weight: 700; font-size: 18px; color: var(--navy);
    z-index: 3;
  }
  .front-photo {
    position: absolute; left: 18px; top: 170px; width: 372px; height: 335px;
    background: linear-gradient(180deg, rgba(255,255,255,1) 0%, rgba(143,182,230,0.8) 28%, #b5bcc4 55%, var(--hull) 75%, #4a6aa8 100%);
  }
  .front-overlay {
    position: absolute; left: 47px; top: 265px; width: 125px; height: 240px;
    background: linear-gradient(90deg, rgba(51,68,184,0.82) 0%, rgba(51,68,184,0.82) 50%, rgba(27,42,107,0.85) 50%);
  }
  .title {
    position: absolute; left: 47px; top: 165px; z-index: 3;
    font-weight: 900; font-size: 28px; line-height: 27px; text-transform: uppercase;
    color: var(--navy); letter-spacing: -0.5px;
  }
  .title__accent { color: var(--red); font-size: 31px; }
  .rule { position: absolute; background: var(--red); z-index: 2; }

  /* Back */
  .back-photo {
    position: absolute; left: 0; top: 127px; width: 244px; height: 378px;
    background: linear-gradient(180deg, var(--sky) 0%, #7f8c8a 35%, #6d7f9a 60%, var(--hull) 80%, #c6c9cd 100%);
  }
  .frame { position: absolute; left: 76px; top: 141px; width: 233px; height: 244px; border: 2px solid var(--red); z-index: 2; }
  .panel {
    position: absolute; left: 119px; top: 192px; width: 271px; height: 313px; z-index: 3;
    background: linear-gradient(160deg, rgba(27,42,107,0.95) 0%, rgba(51,68,184,0.9) 55%, var(--royal-light) 100%);
  }
  .features { list-style: none; position: absolute; left: 150px; top: 228px; z-index: 4; }
  .features li {
    position: relative; padding-left: 11px; color: var(--white);
    font-weight: 700; font-size: 10.5px; line-height: 14px; margin-bottom: 20px;
  }
  .features li:nth-child(3) { margin-bottom: 20px; }
  .features svg { position: absolute; left: 0; top: 3px; width: 8px; height: 8px; }
</style>
</head>
<body>

<section class="page page--front">
  <div class="brand">
    <span class="brand__mark"></span>
    <div class="brand__name">Harbor Compass<small>Marine Services, LLC</small></div>
  </div>
  <p class="course-label">Name of Course:</p>
  <div class="front-photo" role="img" aria-label="Photo of a grey diver support vessel on the water under a blue sky, flag flying from the mast"></div>
  <div class="front-overlay"></div>
  <span class="rule" style="left:0;top:146px;width:212px;height:2px"></span>
  <span class="rule" style="left:210px;top:146px;width:2px;height:61px"></span>
  <span class="rule" style="left:0;top:378px;width:20px;height:2px"></span>
  <h1 class="title">Diver<br>Support<br><span class="title__accent">Vessel Training</span></h1>
</section>

<section class="page page--back">
  <div class="brand">
    <span class="brand__mark"></span>
    <div class="brand__name">Harbor Compass<small>Marine Services, LLC</small></div>
  </div>
  <div class="back-photo" role="img" aria-label="Photo of a sailor in a green jacket at the rail of a vessel, shoreline behind"></div>
  <div class="frame"></div>
  <div class="panel"></div>
  <ul class="features">
    <li><svg viewBox="0 0 10 10"><circle cx="5" cy="5" r="4.2" fill="none" stroke="#fff" stroke-width="1.2"/><path d="M3 5.2l1.5 1.5L8.5 2.5" fill="none" stroke="#fff" stroke-width="1.3"/></svg>To assist Navy Sailors with Becoming<br>More Proficient Coxswains</li>
    <li><svg viewBox="0 0 10 10"><circle cx="5" cy="5" r="4.2" fill="none" stroke="#fff" stroke-width="1.2"/><path d="M3 5.2l1.5 1.5L8.5 2.5" fill="none" stroke="#fff" stroke-width="1.3"/></svg>Focused on Safety &amp; Close-Quarters<br>Maneuvering</li>
    <li><svg viewBox="0 0 10 10"><circle cx="5" cy="5" r="4.2" fill="none" stroke="#fff" stroke-width="1.2"/><path d="M3 5.2l1.5 1.5L8.5 2.5" fill="none" stroke="#fff" stroke-width="1.3"/></svg>Custom Made Course for Specific<br>Users, Scenarios and Vessels Based<br>on OIC Involvement, Client Feedback<br>and After Action Reviews</li>
    <li><svg viewBox="0 0 10 10"><circle cx="5" cy="5" r="4.2" fill="none" stroke="#fff" stroke-width="1.2"/><path d="M3 5.2l1.5 1.5L8.5 2.5" fill="none" stroke="#fff" stroke-width="1.3"/></svg>Taught by Reputable USCG Licensed<br>Boat Captains</li>
    <li><svg viewBox="0 0 10 10"><circle cx="5" cy="5" r="4.2" fill="none" stroke="#fff" stroke-width="1.2"/><path d="M3 5.2l1.5 1.5L8.5 2.5" fill="none" stroke="#fff" stroke-width="1.3"/></svg>Includes Useful Aids</li>
  </ul>
</section>

</body>
</html>
```